Stationery Design Project for a consulting/educational company

We need a stationery design for a consulting / educational company called "VORN d.o.o.". We are an official partner (yet stand-alone company) of the TALMO Institute, Germany (www.talmo-example.de) that covers practically all themes regarding production optimisation, efectiveness, productivity (time studies, workplace organisation,...) We need the design for:

- a CERTIFICATE for seminar participates
- business cards
- letterhead

We are changing our webpage to their design, so we need to change the stationaries as well. I included 2 current logos, one with current color scheme (not important) and the other black/white with a frame. I also included the TALMO original certificate. Only the font + name"VORN" is important, the rest is up to you
Updates

Designs look good, but perhaps a gray & green combo would look nicer? Like on www.talmo-example.de? And without the frames?

Target Market(s)

Larger production companies top and middle management

Industry/Entity Type

Business

Requirements
Must have
• - the stationaries (all of them) should, besides the company name "VORN", also include the logo TALMO (in its color), like on their webpage www.talmo-example.de
Nice to have
• - certificate could use 5th color (e.g. silver) to make an impression
- similar color scheme to www.talmo-example.de

```html
<!DOCTYPE html>
<html lang="en">
<head>
<meta charset="utf-8">
<title>VORN business card</title>
<link rel="stylesheet" href="https://fonts.googleapis.com/css2?family=Lato:wght@400;700;900&display=swap">
<style>
  :root {
    --teal: #17a2a9;
    --teal-dark: #0f8c93;
    --ink: #2e2e2e;
    --text: #555a5c;
    --card: #ffffff;
    --backdrop: #e6e9ea;
  }
  html, body {
    margin: 0;
    padding: 0;
    width: 1200px;
    height: 960px;
    overflow: hidden;
    background: var(--backdrop);
    font-family: "Lato", Arial, sans-serif;
  }
  .canvas {
    position: relative;
    width: 1200px;
    height: 960px;
  }
  .card {
    position: absolute;
    left: 240px;
    width: 720px;
    height: 412px;
    background: var(--card);
    box-shadow: 0 6px 24px rgba(0, 0, 0, 0.12);
    overflow: hidden;
  }
  .card--front { top: 46px; }
  .card--back { top: 502px; }

  .partner-name {
    position: absolute;
    left: 38px;
    top: 30px;
    margin: 0;
    font-size: 66px;
    font-weight: 900;
    letter-spacing: 1px;
    color: var(--ink);
  }
  .accent-bar {
    position: absolute;
    left: 40px;
    top: 124px;
    width: 368px;
    height: 48px;
    background: var(--teal);
  }
  .company-name {
    position: absolute;
    right: 42px;
    top: 34px;
    margin: 0;
    font-size: 62px;
    font-weight: 900;
    letter-spacing: 2px;
    color: var(--text);
  }
  .holder {
    position: absolute;
    left: 318px;
    top: 226px;
    margin: 0;
    color: var(--text);
    font-weight: 400;
  }
  .holder__name { font-size: 34px; }
  .holder__role { font-size: 19px; }

  .contacts {
    position: absolute;
    left: 92px;
    top: 292px;
    margin: 0;
    padding: 0;
    list-style: none;
    font-size: 21px;
    color: var(--text);
  }
  .contacts li {
    display: flex;
    align-items: center;
    gap: 14px;
    height: 30px;
  }
  .contacts svg { width: 20px; height: 20px; }

  .address {
    position: absolute;
    left: 430px;
    top: 282px;
    margin: 0;
    font-style: normal;
    font-size: 18px;
    line-height: 25px;
    color: var(--text);
  }
  .address__web { font-weight: 700; color: var(--ink); }

  .edge-band {
    position: absolute;
    left: 0;
    bottom: 0;
    width: 720px;
    height: 40px;
  }

  .back-mark {
    position: absolute;
    left: 0;
    right: 0;
    top: 110px;
    margin: 0;
    text-align: center;
    font-size: 150px;
    font-weight: 900;
    letter-spacing: 8px;
    color: var(--teal);
  }
</style>
</head>
<body>
<main class="canvas">

  <section class="card card--front" aria-label="Business card front">
    <p class="partner-name">TALMO</p>
    <div class="accent-bar"></div>
    <p class="company-name">VORN</p>

    <p class="holder"><span class="holder__name">Name Surname</span> <span class="holder__role">/ Operation Manager</span></p>

    <ul class="contacts">
      <li>
        <svg viewBox="0 0 20 20" aria-hidden="true"><rect x="2" y="3" width="16" height="15" rx="1.5" fill="none" stroke="var(--teal)" stroke-width="1.6"/><rect x="4.5" y="5.5" width="4" height="10" fill="var(--teal)"/><rect x="10.5" y="6" width="5" height="2" fill="var(--teal)"/><rect x="10.5" y="10" width="5" height="5" fill="none" stroke="var(--teal)" stroke-width="1.4"/></svg>
        (000) 12 345 67 89
      </li>
      <li>
        <svg viewBox="0 0 20 20" aria-hidden="true"><rect x="5" y="2" width="10" height="6" fill="none" stroke="var(--teal)" stroke-width="1.6"/><rect x="2" y="8" width="16" height="7" rx="1.5" fill="var(--teal)"/><rect x="5" y="13" width="10" height="5" fill="#fff" stroke="var(--teal)" stroke-width="1.6"/></svg>
        (000) 12 345 67 90
      </li>
      <li>
        <svg viewBox="0 0 20 20" aria-hidden="true"><rect x="2" y="4" width="16" height="12" fill="none" stroke="var(--teal)" stroke-width="1.6"/><path d="M2 4 L10 11 L18 4 M2 16 L8 10 M18 16 L12 10" fill="none" stroke="var(--teal)" stroke-width="1.6"/></svg>
        name@vorn-example.com
      </li>
    </ul>

    <address class="address">
      Rue des Érables - Val Clair<br>
      BP 512 - City, Country<br>
      <span class="address__web">www.vorn-example.com</span>
    </address>

    <svg class="edge-band" viewBox="0 0 720 40" preserveAspectRatio="none" aria-hidden="true">
      <polygon points="0,18 600,18 578,40 0,40" fill="var(--teal)"/>
      <polygon points="638,18 720,18 720,40 616,40" fill="var(--teal-dark)"/>
    </svg>
  </section>

  <section class="card card--back" aria-label="Business card back">
    <p class="back-mark">VORN</p>
    <svg class="edge-band" viewBox="0 0 720 40" preserveAspectRatio="none" aria-hidden="true">
      <polygon points="0,14 600,14 578,40 0,40" fill="var(--teal)"/>
      <polygon points="640,14 720,14 720,40 618,40" fill="var(--teal-dark)"/>
    </svg>
  </section>

</main>
</body>
</html>
```